Dog care service needs business card design

Our company is Paws Harbour. We provide care for dogs while their owners are away, either through home visits or a holiday stay in the homes of carefully selected minders. Our existing website & Chatterbook cover should provide all the colour cues for our business cards - namely blues, blondes and grey. We have an existing logo (provided).

www.pawsharbourcare.example.au
www.facebook.com/pawsharbourcareau

We wish to clearly communicate our three areas of service "dog minding, home visits, dog walking".

We would like to have the files ready for upload to Printlyne (or similar) for immediate printing.

Target Market(s)

Dog owners who love their dogs like family

Industry/Entity Type

Business

Contact Information for Business Card

Paws Harbour
Ph: 0417 358 904

Font styles to use
Sans Serif

Colors
33a6d7
3176b5

Requirements
Must have
• Logo
• Telephone number
• website
• "Dog minding, home visits, dog walking"
Should not have
• any additional illustrations beyond the logo.

```html
<!DOCTYPE html>
<html lang="en">
<head>
<meta charset="utf-8">
<title>Paws Harbour – Business Card</title>
<link rel="stylesheet" href="https://fonts.googleapis.com/css2?family=Rubik:wght@400;500;700&display=swap">
<style>
  :root {
    --bg: #eeeff2;
    --card: #ffffff;
    --ink: #3a4352;
    --blue: #1f8fd6;
    --blue-deep: #3176b5;
    --faint: #ececee;
  }
  * { margin: 0; padding: 0; box-sizing: border-box; }
  html, body { width: 1200px; height: 600px; overflow: hidden; }
  body {
    background: var(--bg);
    font-family: "Rubik", sans-serif;
    color: var(--ink);
    position: relative;
  }
  .card {
    position: absolute;
    top: 152px;
    width: 467px;
    height: 278px;
    background: var(--card);
    border-radius: 18px;
    box-shadow: 0 6px 18px rgba(0,0,0,0.08);
    overflow: hidden;
  }
  .card--front { left: 93px; }
  .card--back { left: 638px; }

  .brand {
    display: flex;
    align-items: center;
    gap: 10px;
  }
  .brand__mark {
    width: 12px;
    height: 12px;
    background: var(--blue);
    flex: none;
  }
  .brand__name {
    font-weight: 500;
    color: var(--ink);
    letter-spacing: -0.5px;
    white-space: nowrap;
  }
  .card--front .brand {
    position: absolute;
    left: 0; right: 0; top: 0; bottom: 0;
    justify-content: center;
  }
  .card--front .brand__name { font-size: 40px; }

  .card--back .brand {
    position: absolute;
    left: 27px;
    top: 46px;
    gap: 8px;
  }
  .card--back .brand__mark { width: 8px; height: 8px; }
  .card--back .brand__name { font-size: 24px; }

  .backdrop-shape {
    position: absolute;
    right: -60px;
    top: 60px;
    width: 270px;
    height: 270px;
    border-radius: 50%;
    background: var(--faint);
  }

  .contact {
    position: absolute;
    left: 27px;
    top: 126px;
    font-size: 12.5px;
    line-height: 16px;
    color: var(--ink);
  }
  .contact strong { font-weight: 700; }

  .services {
    position: absolute;
    right: 28px;
    top: 161px;
    list-style: none;
    text-align: right;
    font-size: 12px;
    font-weight: 700;
    line-height: 20.5px;
    color: var(--blue);
    letter-spacing: 0.2px;
  }
</style>
</head>
<body>
  <section class="card card--front" aria-label="Card front">
    <div class="brand">
      <span class="brand__mark"></span>
      <span class="brand__name">Paws Harbour</span>
    </div>
  </section>

  <section class="card card--back" aria-label="Card back">
    <div class="backdrop-shape" aria-hidden="true"></div>
    <div class="brand">
      <span class="brand__mark"></span>
      <span class="brand__name">Paws Harbour</span>
    </div>
    <p class="contact">
      Phone: 0417 358 904<br>
      www.<strong>pawsharbourcare</strong>.example.au
    </p>
    <ul class="services">
      <li>DOG MINDING -</li>
      <li>HOME VISITING -</li>
      <li>DOG WALKING -</li>
    </ul>
  </section>
</body>
</html>
```